Automotive component supplier needs a business card design

We need a business card design for our company called Velmar Global Components Ltd based in the UK. We are a supplier of interior and exterior components to premium car manufacturers such as Corvane Hale, Durrant Fyfe, Maxtorn and Valdessimo. We would like to see a modern business card design that uses the colour blue.

Target Market(s)

Premium automotive car manufacturers.

Industry/Entity Type

Automotive

Contact Information for Business Card

Company Name : Velmar Global Components Limited
Address: 17 Tamsey Yard, Upper Drisk, Warwick, CV31 8RJ, United Kingdom
Web Address : www.velmarparts-example.co.uk

Font styles to use
Other font styles liked:
• Helvetica

Colors
3176b5
0255a3
85acd3
cfdeed
cee9f5
85cae6
34a6d7
0692cd
9bcb3c

Requirements
Must have
• Clear company logo and a mixture of blue colours.
Nice to have
• A high quality modern image.
Should not have
• Multiple colours.

```html
<!DOCTYPE html>
<html lang="en">
<head>
<meta charset="utf-8">
<title>Velmar Global Components – Business Card</title>
<link rel="stylesheet" href="https://fonts.googleapis.com/css2?family=Open+Sans:wght@300;400;700&display=swap">
<style>
  :root {
    --backdrop: #9b9b9b;
    --card-white: #ffffff;
    --card-offwhite: #f5f6f7;
    --brand-blue: #1b98d5;
    --teal: #27a3bb;
    --slate: #2a4d63;
    --navy: #282f45;
    --deep-blue: #2e3d5b;
    --ink: #2a4a63;
    --white: #ffffff;
  }
  html, body {
    margin: 0;
    padding: 0;
    width: 1200px;
    height: 1000px;
    overflow: hidden;
    background: var(--backdrop);
    font-family: "Open Sans", Helvetica, Arial, sans-serif;
  }
  .canvas {
    position: relative;
    width: 1200px;
    height: 1000px;
  }
  .card {
    position: absolute;
    display: block;
  }
  .card--front { left: 168px; top: 89px; width: 678px; height: 384px; }
  .card--back  { left: 409px; top: 562px; width: 679px; height: 388px; }

  .wordmark-name, .wordmark-tagline { fill: var(--brand-blue); font-weight: 700; }
  .wordmark-name { font-size: 64px; letter-spacing: 2px; }
  .wordmark-tagline { font-size: 13.5px; letter-spacing: 6px; }

  .person-name { fill: var(--ink); font-size: 38px; }
  .person-name .first { font-weight: 300; }
  .person-name .last { font-weight: 700; }
  .person-role { fill: var(--teal); font-size: 15px; font-weight: 400; }

  .contact-text { fill: var(--white); font-size: 16px; font-weight: 400; }
  .contact-icon circle { fill: none; stroke: var(--white); stroke-width: 2; }
  .contact-icon .glyph { fill: var(--white); }
  .contact-icon .glyph-line { fill: none; stroke: var(--white); stroke-width: 1.4; }
</style>
</head>
<body>
<main class="canvas">

  <!-- Front of card -->
  <svg class="card card--front" viewBox="0 0 678 384" xmlns="http://www.w3.org/2000/svg" aria-label="Business card front">
    <defs>
      <linearGradient id="front-top-tone" x1="0" y1="0" x2="1" y2="0">
        <stop offset="0" stop-color="var(--navy)"/>
        <stop offset="1" stop-color="var(--teal)"/>
      </linearGradient>
      <linearGradient id="front-bottom-tone" x1="1" y1="0" x2="0" y2="0">
        <stop offset="0" stop-color="var(--navy)"/>
        <stop offset="1" stop-color="var(--teal)"/>
      </linearGradient>
      <linearGradient id="back-side-tone" x1="0" y1="0" x2="1" y2="0">
        <stop offset="0" stop-color="var(--teal)"/>
        <stop offset="0.5" stop-color="var(--slate)"/>
        <stop offset="1" stop-color="var(--deep-blue)"/>
      </linearGradient>
    </defs>
    <rect class="card-face" width="678" height="384" fill="var(--card-white)"/>
    <path class="corner-area corner-area--top" role="img" aria-label="Decorative corner artwork in blue tones"
          d="M392,0 C430,80 520,140 678,176 L678,0Z" fill="url(#front-top-tone)"/>
    <path class="corner-area corner-area--bottom" role="img" aria-label="Decorative corner artwork in blue tones"
          d="M0,211 C150,225 262,280 287,384 L0,384Z" fill="url(#front-bottom-tone)"/>
    <g class="wordmark">
      <text class="wordmark-name" x="356" y="197" text-anchor="middle">VELMAR</text>
      <text class="wordmark-tagline" x="359" y="219" text-anchor="middle">GLOBAL COMPONENTS</text>
    </g>
  </svg>

  <!-- Back of card -->
  <svg class="card card--back" viewBox="0 0 679 388" xmlns="http://www.w3.org/2000/svg" aria-label="Business card back">
    <rect class="card-face" width="679" height="388" fill="var(--card-offwhite)"/>
    <path class="side-area" role="img" aria-label="Decorative side artwork in blue tones"
          d="M250,388 C280,200 360,40 600,0 L679,0 L679,388Z" fill="url(#back-side-tone)"/>

    <g class="identity">
      <text class="person-name" x="264" y="203" text-anchor="end"><tspan class="first">JOHN </tspan><tspan class="last">DOE</tspan></text>
      <text class="person-role" x="251" y="228" text-anchor="end">GRAPHIC DESIGNER</text>
    </g>

    <g class="contact-list">
      <g class="contact-icon contact-icon--email" transform="translate(387,119)">
        <circle r="15"/>
        <rect class="glyph" x="-8" y="-6" width="16" height="11" rx="1"/>
        <path d="M-8,-5 L0,1 L8,-5" fill="none" stroke="var(--deep-blue)" stroke-width="1.5"/>
      </g>
      <text class="contact-text" x="416" y="128">info@velmarparts-example.co.uk</text>

      <g class="contact-icon contact-icon--phone" transform="translate(352,179)">
        <circle r="15"/>
        <path class="glyph" d="M-6,-8 L-3,-8 L-1,-3 L-3,-1 C-2,2 1,4 2,4 L4,2 L8,4 L8,7 C8,8 7,9 5,9 C-2,8 -8,2 -8,-5 C-8,-7 -7,-8 -6,-8Z"/>
      </g>
      <text class="contact-text" x="380" y="177">+00 1234 5678 9012</text>
      <text class="contact-text" x="380" y="194">+00 1234 5678 9012</text>

      <g class="contact-icon contact-icon--address" transform="translate(322,244)">
        <circle r="15"/>
        <path class="glyph" d="M0,-9 L-9,-1 L-6,-1 L-6,8 L-2,8 L-2,3 L2,3 L2,8 L6,8 L6,-1 L9,-1Z"/>
      </g>
      <text class="contact-text" x="352" y="242">17 Tamsey Yard, Upper Drisk,</text>
      <text class="contact-text" x="352" y="262">Warwick, CV31 8RJ, United Kingdom</text>

      <g class="contact-icon contact-icon--web" transform="translate(303,311)">
        <circle r="15"/>
        <circle class="glyph-line" r="8"/>
        <ellipse class="glyph-line" rx="3.5" ry="8"/>
        <line class="glyph-line" x1="-8" y1="0" x2="8" y2="0"/>
      </g>
      <text class="contact-text" x="334" y="317">www.velmarparts-example.co.uk</text>
    </g>
  </svg>

</main>
</body>
</html>
```